Postcard Design

We need a postcard design for a private lender in the Denver area. We are offering hard money loans and loans for those doing fix-and-flips. We definitely want something that is Colorado-specific, maybe a view of downtown Denver? We are not offering small personal loans, but we are also not lending over 800k. Our audience is not major corporations. all the info in the old postcard is correct EXCEPT:

the new email should be thimble417@postvane.net

We would like to omit all use of exclamation points.

```html
<!DOCTYPE html>
<html lang="en">
<head>
<meta charset="utf-8">
<title>Larkspur Lending Inc. – Hard Money Loans Postcard</title>
<link rel="stylesheet" href="https://fonts.googleapis.com/css2?family=Roboto+Condensed:wght@400;700&family=Open+Sans:wght@400;700&family=Oswald:wght@600&family=Lora&family=Rokkitt:wght@700&display=swap">
<style>
  :root {
    --stage: #7d5f42;
    --blue: #1e93bd;
    --blue-deep: #137aa3;
    --green: #12914a;
    --ink: #1a1a1a;
    --dark: #222222;
    --white: #ffffff;
    --stamp: #4a4a4a;
  }
  * { margin: 0; padding: 0; box-sizing: border-box; }
  html, body { width: 907px; height: 1200px; overflow: hidden; }
  body { background: var(--stage); position: relative; font-family: "Open Sans", sans-serif; }

  .card { position: absolute; width: 708px; height: 548px; overflow: hidden; }
  .card-front { left: 95px; top: 42px; background: linear-gradient(180deg, var(--blue) 0%, var(--blue-deep) 100%); }
  .card-back { left: 92px; top: 615px; background: var(--white); }
  .card svg.shapes { position: absolute; left: 0; top: 0; }
  .card > * { position: absolute; white-space: nowrap; }

  .brand-title { right: 33px; top: 22px; font: 700 40px/1 "Roboto Condensed", sans-serif; color: var(--white); letter-spacing: 1.8px; }
  .headline-hard { left: 18px; top: 112px; font: 700 38px/1 "Roboto Condensed", sans-serif; color: var(--dark); }
  .headline-money { left: 15px; top: 132px; font: 700 130px/1 "Rokkitt", serif; color: var(--green); transform: scaleX(0.91); transform-origin: left top; }
  .headline-loans { left: 433px; top: 196px; font: 700 40px/1 "Roboto Condensed", sans-serif; color: var(--dark); }

  .features { list-style: none; color: var(--white); font-size: 16px; line-height: 21px; white-space: normal; }
  .features li { position: relative; padding-left: 19px; margin-bottom: 7px; }
  .features li::before { content: ""; position: absolute; left: 0; top: 5px; width: 10px; height: 10px; background: var(--green); }
  .features-left { left: 18px; top: 298px; width: 345px; }
  .features-right { left: 403px; top: 298px; width: 290px; }

  .cta-kicker { left: 331px; top: 432px; font: 400 11px/1 "Lora", serif; color: var(--green); }
  .cta-line { left: 331px; top: 446px; font: 700 22px/1 "Roboto Condensed", sans-serif; color: var(--white); }
  .cta-phone { left: 487px; top: 430px; font: 400 39px/1 "Roboto Condensed", sans-serif; color: var(--blue); transform: scaleX(0.79); transform-origin: left top; }

  .tagline-top { left: 17px; top: 476px; font: 700 22px/1 "Roboto Condensed", sans-serif; color: var(--white); }
  .tagline-bottom { left: 17px; top: 502px; font: 400 19px/1 "Roboto Condensed", sans-serif; color: var(--dark); }

  .contact { display: flex; align-items: center; gap: 6px; font: 700 16px/1 "Roboto Condensed", sans-serif; color: var(--white); letter-spacing: 0.4px; }
  .contact svg { flex: none; }
  .front-email { left: 252px; top: 510px; }
  .front-web { left: 482px; top: 510px; }

  .return-name { left: 17px; top: 24px; font: 700 16px/1 "Roboto Condensed", sans-serif; color: var(--green); }
  .return-address { left: 17px; top: 44px; font: 400 16px/21px "Open Sans", sans-serif; color: var(--ink); font-style: normal; }
  .stamp-box { left: 609px; top: 17px; width: 78px; height: 91px; background: var(--stamp); }

  .offer-lead { left: 17px; top: 98px; font: 600 96px/1 "Oswald", sans-serif; color: var(--green); transform: scaleX(0.79); transform-origin: left top; }
  .offer-mid { left: 18px; top: 206px; font: 400 44px/1 "Lora", serif; color: var(--ink); }
  .offer-sub { left: 18px; top: 251px; font: 700 29px/1 "Open Sans", sans-serif; color: var(--green); }

  .back-phone { left: 36px; top: 323px; font: 400 40px/1 "Roboto Condensed", sans-serif; color: var(--blue); transform: scaleX(0.78); transform-origin: left top; }
  .back-email { left: 14px; top: 364px; }
  .back-web { left: 14px; top: 388px; }
</style>
</head>
<body>

<section class="card card-front" aria-label="Postcard front">
  <svg class="shapes" width="708" height="548" viewBox="0 0 708 548" aria-hidden="true">
    <polygon points="0,98 452,98 587,151 708,151 708,283 0,283" fill="var(--white)"/>
    <polyline points="0,91 450,91 585,144 708,144" fill="none" stroke="var(--green)" stroke-width="7"/>
    <polygon points="0,247 585,247 610,275 0,275" fill="var(--blue)"/>
    <polygon points="588,247 612,247 640,275 616,275" fill="var(--blue)"/>
    <polygon points="622,247 646,247 674,275 650,275" fill="var(--blue)"/>
    <polygon points="0,283 708,283 708,482 290,482 160,432 0,432" fill="var(--ink)"/>
    <polyline points="0,438 158,438 288,488 708,488" fill="none" stroke="var(--green)" stroke-width="6"/>
    <polyline points="0,446 156,446 286,496 708,496" fill="none" stroke="var(--white)" stroke-width="3"/>
  </svg>

  <h1 class="brand-title">Larkspur Lending Inc.</h1>
  <div class="headline-hard">Hard</div>
  <div class="headline-money">MONEY</div>
  <div class="headline-loans">Loans</div>

  <ul class="features features-left">
    <li>We are loaning our own funds</li>
    <li>We do a variety of real estate secured loans including loans to buy foreclosures, short sales &amp; more.</li>
    <li>Loan rates from 8%</li>
  </ul>
  <ul class="features features-right">
    <li>Fix &amp; flip Loans at 10%</li>
    <li>No appraisal, processing fees or "junk" fees</li>
    <li>Fast closing</li>
  </ul>

  <div class="cta-kicker">PRIVATE MONEY FOR</div>
  <div class="cta-line">less call an at</div>
  <div class="cta-phone">303-555-0147</div>

  <div class="tagline-top">Denver Private</div>
  <div class="tagline-bottom">Money Lender</div>

  <div class="contact front-email">
    <svg width="11" height="8" viewBox="0 0 11 8" aria-hidden="true"><rect width="11" height="8" fill="var(--white)"/><polyline points="0,0 5.5,4.5 11,0" fill="none" stroke="var(--ink)" stroke-width="1"/></svg>
    thimble417@postvane.net
  </div>
  <div class="contact front-web">
    <svg width="10" height="10" viewBox="0 0 10 10" aria-hidden="true"><circle cx="5" cy="5" r="4.3" fill="none" stroke="var(--white)" stroke-width="1.2"/><line x1="0.7" y1="5" x2="9.3" y2="5" stroke="var(--white)"/><ellipse cx="5" cy="5" rx="1.8" ry="4.3" fill="none" stroke="var(--white)"/></svg>
    larkspurlendinginc.com
  </div>
</section>

<section class="card card-back" aria-label="Postcard back">
  <svg class="shapes" width="708" height="548" viewBox="0 0 708 548" aria-hidden="true">
    <polygon points="0,307 340,307 340,322 144,436 0,452" fill="var(--ink)"/>
    <polyline points="346,0 346,325 148,443 0,458" fill="none" stroke="var(--green)" stroke-width="7"/>
    <polyline points="355,0 355,331 152,459 0,472" fill="none" stroke="var(--blue)" stroke-width="6"/>
  </svg>

  <div class="return-name">Larkspur Lending,Inc.</div>
  <address class="return-address">412 Alder Row<br>Denver, CO 80202</address>
  <div class="stamp-box" aria-label="Stamp area"></div>

  <div class="offer-lead">LOW COST</div>
  <div class="offer-mid">HARD MONEY</div>
  <div class="offer-sub">REAL ESTATE LOANS</div>

  <div class="back-phone">303-555-0147</div>
  <div class="contact back-email">
    <svg width="11" height="8" viewBox="0 0 11 8" aria-hidden="true"><rect width="11" height="8" fill="var(--white)"/><polyline points="0,0 5.5,4.5 11,0" fill="none" stroke="var(--ink)" stroke-width="1"/></svg>
    thimble417@postvane.net
  </div>
  <div class="contact back-web">
    <svg width="10" height="10" viewBox="0 0 10 10" aria-hidden="true"><circle cx="5" cy="5" r="4.3" fill="none" stroke="var(--white)" stroke-width="1.2"/><line x1="0.7" y1="5" x2="9.3" y2="5" stroke="var(--white)"/><ellipse cx="5" cy="5" rx="1.8" ry="4.3" fill="none" stroke="var(--white)"/></svg>
    larkspurlendinginc.com
  </div>
</section>

</body>
</html>
```